ZiPU Vortal Bhutan Trip

This is a one-page (A5) flyer to attract sign ups for Bhutan Trip.

Target Market(s)

Young entrepreneurs (worldwide)

Requirements
Must have
• Must have "WOW" effect and attract sign ups
Nice to have
• Striking and vibrant

```html
<!DOCTYPE html>
<html lang="en">
<head>
<meta charset="utf-8">
<title>ZiPU Vortal Bhutan Trip</title>
<link rel="stylesheet" href="https://fonts.googleapis.com/css2?family=Alfa+Slab+One&family=Oswald:wght@500;600;700&family=Roboto:wght@700&family=Roboto+Condensed:wght@400&family=Noto+Serif:ital,wght@1,700&display=swap">
<style>
:root{
  --page:#dfe3e7;
  --paper:#ffffff;
  --maroon:#7f1416;
  --maroon-text:#8a1a1a;
  --orange:#f6921e;
  --orange-text:#f5a03a;
  --red:#e0222a;
  --ink:#222222;
  --polaroid:#fbfbfb;
}
*{margin:0;padding:0;box-sizing:border-box}
html,body{width:1200px;height:1200px;overflow:hidden;background:var(--page)}
.flyer{position:absolute;left:212px;top:57px;width:776px;height:1086px;background:var(--paper);overflow:hidden;box-shadow:0 6px 24px rgba(0,0,0,.25)}
.abs{position:absolute}
.brand{left:0;width:776px;top:102px;text-align:center;font-family:"Oswald",sans-serif;font-weight:600;font-size:54px;color:var(--ink);letter-spacing:1px}
.title{left:0;width:776px;top:190px;text-align:center;font-family:"Alfa Slab One",serif;font-weight:400;font-size:76px;color:var(--orange);line-height:1;
  text-shadow:3px 0 0 var(--maroon),-3px 0 0 var(--maroon),0 3px 0 var(--maroon),0 -3px 0 var(--maroon),2px 2px 0 var(--maroon),-2px 2px 0 var(--maroon),2px -2px 0 var(--maroon),-2px -2px 0 var(--maroon)}
.ribbon{left:198px;top:286px;width:380px;height:50px}
.ribbon-text{left:230px;top:286px;width:317px;height:50px;text-align:center;font-family:"Oswald",sans-serif;font-weight:700;font-size:44px;line-height:50px;color:#fff}
.tagline{left:0;width:776px;top:346px;text-align:center;font-family:"Roboto",sans-serif;font-weight:700;font-size:21.5px;line-height:27px;color:var(--maroon-text)}
.band-left{left:0;top:608px;width:388px;height:478px;background:var(--maroon)}
.band-price{left:388px;top:608px;width:388px;height:182px;background:var(--orange)}
.band-register{left:388px;top:790px;width:388px;height:112px;background:var(--maroon)}
.polaroid{background:var(--polaroid);width:190px;height:240px;box-shadow:2px 4px 10px rgba(0,0,0,.35);padding:10px 10px 44px}
.polaroid .photo{width:100%;height:100%}
.p1{left:18px;top:404px;transform:rotate(-5deg)}
.p2{left:202px;top:404px;transform:rotate(3deg)}
.p3{left:378px;top:404px;transform:rotate(-6deg)}
.p4{left:574px;top:408px;transform:rotate(7deg)}
.photo-temple{background:linear-gradient(#9fbbd8 0%,#b8cde0 30%,#8c3326 45%,#b9a995 75%,#9a8d7a 100%)}
.photo-group{background:linear-gradient(#8c8f94 0%,#6b4a3e 40%,#5a2d26 70%,#3f3a35 100%)}
.photo-dzong{background:linear-gradient(#c9d3dc 0%,#5f7a4a 30%,#8a3a2c 60%,#d9d2c4 80%,#6d6a5e 100%)}
.photo-bridge{background:linear-gradient(#6e8f52 0%,#8aa86a 40%,#b9b4aa 70%,#7a7f6d 100%)}
.benefits{left:80px;top:645px;width:300px;list-style:none}
.benefits li{height:53px}
.benefits .verb{display:block;font-family:"Oswald",sans-serif;font-weight:500;font-size:25px;line-height:26px;color:var(--orange-text)}
.benefits .detail{display:block;font-family:"Roboto Condensed",sans-serif;font-size:18.5px;line-height:21px;color:#fff}
.price{left:388px;width:388px;top:650px;text-align:center;font-family:"Noto Serif",serif;font-style:italic;font-weight:700;font-size:30px;line-height:32px;color:#fff}
.early{left:388px;width:388px;top:683px;text-align:center;font-family:"Oswald",sans-serif;font-weight:700;font-size:27px;line-height:34px;color:var(--maroon);
  text-shadow:2px 0 0 #fff,-2px 0 0 #fff,0 2px 0 #fff,0 -2px 0 #fff,1.5px 1.5px 0 #fff,-1.5px 1.5px 0 #fff,1.5px -1.5px 0 #fff,-1.5px -1.5px 0 #fff}
.deadline{left:404px;top:754px;width:290px;height:28px;border-radius:6px;background:var(--red);text-align:center;font-family:"Noto Serif",serif;font-style:italic;font-weight:700;font-size:16.5px;line-height:28px;color:#fff}
.register{left:388px;width:388px;top:794px;text-align:center;font-family:"Oswald",sans-serif;font-weight:700;font-size:35px;line-height:40px;color:#fff}
.limit{left:388px;width:388px;top:833px;text-align:center;font-family:"Noto Serif",serif;font-style:italic;font-weight:700;font-size:22px;line-height:28px;color:#fff}
.email{left:388px;width:388px;top:862px;text-align:center;font-family:"Noto Serif",serif;font-style:italic;font-weight:700;font-size:26px;line-height:32px;color:var(--orange-text)}
.supported{left:388px;width:388px;top:907px;text-align:center;font-family:"Oswald",sans-serif;font-weight:600;font-size:25px;line-height:34px;color:var(--ink)}
.sponsors{left:398px;width:370px;top:966px;display:flex;justify-content:space-around;list-style:none}
.sponsors li{display:flex;align-items:center;gap:5px;font-family:"Roboto Condensed",sans-serif;font-size:14px;color:var(--ink)}
.sponsors .dot{width:10px;height:10px;border-radius:50%;background:var(--maroon)}
</style>
</head>
<body>
<main class="flyer">
  <div class="abs brand">ZiPU Vortal</div>
  <h1 class="abs title">Bhutan Trip</h1>

  <svg class="abs ribbon" viewBox="0 0 380 50" aria-hidden="true">
    <polygon points="0,12 40,12 40,44 0,44 16,28" fill="var(--red)"/>
    <polygon points="380,12 340,12 340,44 380,44 364,28" fill="var(--red)"/>
    <rect x="32" y="0" width="317" height="50" fill="var(--red)"/>
  </svg>
  <div class="abs ribbon-text">3-6 JULY 2017</div>

  <p class="abs tagline">Sign Up For A Once In A Lifetime Experience In<br>The Land Of Happiness!</p>

  <div class="abs band-left"></div>
  <div class="abs band-price"></div>
  <div class="abs band-register"></div>

  <figure class="abs polaroid p1"><div class="photo photo-temple" role="img" aria-label="Photo of a Bhutanese temple courtyard with a monk walking"></div></figure>
  <figure class="abs polaroid p2"><div class="photo photo-group" role="img" aria-label="Group photo of trip participants in traditional dress"></div></figure>
  <figure class="abs polaroid p3"><div class="photo photo-dzong" role="img" aria-label="Photo of a dzong fortress in a green valley"></div></figure>
  <figure class="abs polaroid p4"><div class="photo photo-bridge" role="img" aria-label="Photo of a prayer-flag bridge leading to a mountain temple"></div></figure>

  <ul class="abs benefits">
    <li><span class="verb">LEARN</span><span class="detail">From Leading Social Change Makers</span></li>
    <li><span class="verb">DISCOVER</span><span class="detail">Your Inner Happiness</span></li>
    <li><span class="verb">IMMERSE</span><span class="detail">In Traditional Sports And Craft</span></li>
    <li><span class="verb">ENGAGE</span><span class="detail">The Community Through Volunteering</span></li>
    <li><span class="verb">SAVOUR</span><span class="detail">Organic Food</span></li>
    <li><span class="verb">EXPERIENCE</span><span class="detail">Warm Bhutanese Hospitality</span></li>
    <li><span class="verb">REJUVENATE</span><span class="detail">Your Mind, Body And Soul</span></li>
  </ul>

  <div class="abs price">Price at USD2800</div>
  <div class="abs early">EARLY BIRD DISCOUNT<br>USD2300</div>
  <div class="abs deadline">If you sign up by 31 March 2017</div>

  <div class="abs register">REGISTER NOW!</div>
  <div class="abs limit">Limited to 30 participants!</div>
  <div class="abs email">hello@lumenfund.org</div>

  <div class="abs supported">SUPPORTED BY</div>
  <ul class="abs sponsors">
    <li><span class="dot"></span>Lumen Fund</li>
    <li><span class="dot"></span>Trailvane</li>
    <li><span class="dot"></span>Banyan Circle</li>
  </ul>
</main>
</body>
</html>
```